Webdesign for an Health & Beauty Center

We need a new modern and elegant web design for the relaunch of the http://veskarin.at/ website.
The website is for a company which offer all services for a beuty center like epilation, cosmetics and more.
The new website should use big emotional background images and a modern menu.
All in all the website should give a female expression and the design should be clear and not playful.
The existing logo used be used for the new design, the base colours of the existing website could be used optionally.

Reason: Review of the designs together with the customer needs a little more time.

Industry/Entity Type
It Company
Look and feel
Each slider illustrates characteristics of the customer's brand and the style your logo design should communicate.

```html
<!DOCTYPE html>
<html lang="de">
<head>
<meta charset="utf-8">
<title>Veskarin Health &amp; Beauty Center</title>
<link rel="stylesheet" href="https://fonts.googleapis.com/css2?family=Open+Sans:wdth,wght@75..100,300..700&display=swap">
<style>
:root{
  --beige:#eee2c8;
  --beige-light:#f6efe0;
  --page:#f7f9f9;
  --gold:#bba874;
  --gold-dark:#a8945e;
  --tile:#c6ab70;
  --tile-dark:#928566;
  --pink:#c27f9b;
  --pink-dark:#a9657f;
  --text:#7b6e58;
  --muted:#8d8d8d;
  --field:#e8e6ea;
  --bar:#ece3d4;
}
*{margin:0;padding:0;box-sizing:border-box}
html,body{width:949px;height:1200px;overflow:hidden}
body{position:relative;background:var(--page);font-family:"Open Sans",sans-serif;color:var(--muted)}
.cond{font-family:"Open Sans",sans-serif;font-stretch:75%;font-weight:300}
.backdrop{position:absolute;left:0;top:0;width:949px;height:525px;background:linear-gradient(90deg,var(--beige) 0%,var(--beige-light) 50%,var(--beige) 100%)}
.header{position:absolute;left:126px;top:0;width:697px;height:97px;background:#fff;box-shadow:0 1px 3px rgba(0,0,0,.15)}
.brand-name{position:absolute;font-family:"Open Sans",sans-serif;font-weight:400;color:var(--text);white-space:nowrap}
.header .brand-name{left:22px;top:30px;font-size:26px;line-height:34px}
.topinfo{position:absolute;top:14px;font-size:9px;color:var(--muted);display:flex;align-items:center;gap:6px}
.topinfo svg{fill:var(--pink)}
.nav{position:absolute;top:64px;left:0;font-size:13px;color:var(--text);text-transform:uppercase}
.nav span{position:absolute;white-space:nowrap}
.nav .active{color:var(--pink)}
.nav .active:after{content:"";position:absolute;left:-2px;right:-2px;top:29px;height:3px;background:var(--pink)}
.hero-photo{position:absolute;left:126px;top:97px;width:406px;height:340px;background:radial-gradient(ellipse at 55% 45%,#e9cdb8 0%,#dcb79d 40%,#efe3cf 80%)}
.hero-title{position:absolute;left:560px;top:200px;font-size:36px;color:var(--text);white-space:nowrap}
.hero-sub{position:absolute;left:566px;top:248px;font-size:13px;line-height:20px;color:var(--text);font-weight:300}
.btn{position:absolute;background:linear-gradient(#d497af,var(--pink-dark));color:#fff;text-align:center;border-bottom:2px solid #95506b}
.hero-btn{left:563px;top:314px;width:163px;height:32px;font-size:17px;line-height:31px}
.panel{position:absolute;left:126px;top:437px;width:697px;height:645px;background:#fff;box-shadow:0 1px 3px rgba(0,0,0,.15)}
.welcome{position:absolute;left:146px;top:462px;font-size:24px;color:var(--text);white-space:nowrap}
.welcome-photo{position:absolute;left:145px;top:502px;width:396px;height:139px;border-radius:3px;background:linear-gradient(90deg,#2c3338 0%,#4a5660 45%,#8e9fae 70%,#b8c5cf 100%)}
.copy{position:absolute;left:143px;top:656px;width:405px;font-size:10px;line-height:15.6px;color:var(--muted)}
.copy p+p{margin-top:15px}
.booking{position:absolute;left:586px;top:466px;width:215px;height:285px;background:var(--field)}
.booking-head{height:34px;background:var(--gold);color:#fff;font-size:18px;line-height:34px;padding-left:44px;position:relative}
.booking-head svg{position:absolute;left:19px;top:9px}
.booking-head:after{content:"";position:absolute;right:0;bottom:-8px;border-left:8px solid transparent;border-top:8px solid var(--gold-dark)}
.field{position:absolute;left:20px;width:176px;height:25px;background:#fff;font-size:9.5px;line-height:25px;padding-left:8px;color:var(--muted)}
.booking .btn{left:20px;top:228px;width:176px;height:40px;font-size:13px;line-height:39px}
.services-title{position:absolute;left:143px;top:768px;width:658px;height:28px;text-align:center}
.services-title:before{content:"";position:absolute;left:0;right:0;top:14px;height:4px;border-top:1px solid #ddd;border-bottom:1px solid #ddd}
.services-title span{position:relative;background:#fff;padding:0 6px;font-size:24px;color:var(--text);line-height:28px}
.tile{position:absolute;width:157px;height:118px;color:#fff;text-align:center;display:flex;align-items:center;justify-content:center;font-size:16px;line-height:22px;background:linear-gradient(135deg,#d8c08a,var(--tile) 55%,#b39a62)}
.tile.info{background:var(--tile-dark);display:block;text-align:left;padding:20px 13px;font-size:10px;line-height:15.5px;font-family:"Open Sans",sans-serif;font-stretch:100%;font-weight:400}
.tile.info .link{position:absolute;left:13px;bottom:18px;font-size:13px;font-stretch:75%;font-weight:300}
.foot-brand{left:136px;top:1112px;font-size:22px;line-height:30px}
.foot-info{position:absolute;font-size:8.5px;line-height:18px;color:var(--muted)}
.foot-info svg{fill:#aaa;position:absolute;left:-16px}
.social{position:absolute;top:1105px;width:22px;height:22px;border-radius:50%;background:#dedede}
.bottom-bar{position:absolute;left:0;top:1174px;width:949px;height:26px;background:var(--bar);font-size:8px;color:#b3a78f;line-height:26px}
</style>
</head>
<body>
<div class="backdrop"></div>

<header class="header">
  <div class="brand-name">Veskarin</div>
  <div class="topinfo" style="left:250px">
    <svg width="12" height="11" viewBox="0 0 12 11"><path d="M6 0L0 5.5h1.6V11h3.2V7.5h2.4V11h3.2V5.5H12z"/></svg>
    123 Your Street, Your Avenue, Your Country
  </div>
  <div class="topinfo" style="left:464px">
    <svg width="16" height="10" viewBox="0 0 16 10"><rect x="4.5" y="0.5" width="11" height="9" fill="none" stroke="#c27f9b"/><path d="M4.5 .5l5.5 5 5.5-5" fill="none" stroke="#c27f9b"/><rect x="0" y="2" width="3" height="1"/><rect x="1" y="5" width="2" height="1"/></svg>
    hallo@veskarin-mail.at
  </div>
  <div class="topinfo" style="left:586px">
    <svg width="11" height="11" viewBox="0 0 11 11"><path d="M2 0l2 2.5-1 1.5c.8 1.8 2 3 3.5 3.5l1.5-1L11 8.5 9.5 11C4.5 10.5.5 6.5 0 1.5z"/></svg>
    +43 555 010 200
  </div>
  <nav class="nav cond">
    <span class="active" style="left:248px">Über uns</span>
    <span style="left:310px">Leistungen</span>
    <span style="left:381px">Galerie</span>
    <span style="left:434px">Pflegelinie</span>
    <span style="left:504px">Angebote</span>
    <span style="left:568px">Preislisten</span>
    <span style="left:638px">Kontakt</span>
  </nav>
</header>

<div class="hero-photo" role="img" aria-label="Portrait photo of a woman with clear skin touching her cheek"></div>
<h1 class="hero-title cond">Gesundheit ist Schön!</h1>
<p class="hero-sub">Your Veskarin expert give you personal advice<br>&amp; promotes your health and beauty!</p>
<div class="btn hero-btn cond">Contact Us</div>

<main class="panel"></main>
<h2 class="welcome cond">Welcome to Veskarin Health &amp; Beauty Center</h2>
<div class="welcome-photo" role="img" aria-label="Photo of the salon storefront at night with illuminated sign and new-opening lettering on the glass"></div>
<div class="copy">
  <p>Lorem ipsum dolor sit amet, consectetur adipisicing elit, sed do eiusmod tempor incididunt ut labore et dolore magna aliqua. Ut enim ad minim veniam, quis nostrud exercitation ullamco laboris nisi ut aliquip ex ea commodo consequat.</p>
  <p>Duis aute irure dolor in reprehenderit in voluptate velit esse cillum dolore eu fugiat nulla pariatur.</p>
</div>

<section class="booking">
  <div class="booking-head cond">
    <svg width="15" height="15" viewBox="0 0 15 15"><rect x="1" y="2.5" width="13" height="11.5" fill="none" stroke="#fff" stroke-width="1.4"/><rect x="1" y="2.5" width="13" height="3" fill="#fff"/><g fill="#fff"><rect x="3" y="7" width="2" height="2"/><rect x="6.5" y="7" width="2" height="2"/><rect x="10" y="7" width="2" height="2"/><rect x="3" y="10.5" width="2" height="2"/><rect x="6.5" y="10.5" width="2" height="2"/></g></svg>
    Book An Appointment
  </div>
  <div class="field" style="top:56px">Select Service
    <span style="position:absolute;right:0;top:0;width:25px;height:25px;border-left:1px solid #e2e2e2"></span>
    <svg style="position:absolute;right:9px;top:11px" width="7" height="4" viewBox="0 0 7 4"><path d="M0 0h7L3.5 4z" fill="#999"/></svg>
  </div>
  <div class="field" style="top:89px">Full Name</div>
  <div class="field" style="top:122px">Email</div>
  <div class="field" style="top:155px">Phone</div>
  <div class="field" style="top:189px">Date of Appointment (required)
    <svg style="position:absolute;right:6px;top:6px" width="13" height="13" viewBox="0 0 13 13"><rect x=".5" y="1.5" width="12" height="11" fill="#f3ead6" stroke="#bba874"/><rect x=".5" y="1.5" width="12" height="3" fill="#bba874"/></svg>
  </div>
  <div class="btn">Submit Form</div>
</section>

<div class="services-title"><span class="cond">Our Services</span></div>

<div class="tile cond" style="left:147px;top:806px" role="img" aria-label="SHR-IPL laser hair removal photo">SHR-IPL<br>(Laser-Haarentfernung)</div>
<div class="tile cond" style="left:313px;top:806px" role="img" aria-label="Cavitation body treatment photo">Kavitation<br>(gegen Fettpölsterchen)</div>
<div class="tile info" style="left:478px;top:806px">Jeder gewünschte Muskel wird gezielt trainiert und gestrafft!<span class="link">Tonaflex »</span></div>
<div class="tile cond" style="left:643px;top:806px" role="img" aria-label="Microdermabrasion treatment photo">Thermaglow<br>(Mikro-Dermabrasion,<br>Hautglättung)</div>
<div class="tile cond" style="left:231px;top:934px" role="img" aria-label="Oxygen facial treatment photo">Aero-Oxy<br>(Sauerstoffbehandlung)</div>
<div class="tile cond" style="left:397px;top:934px" role="img" aria-label="Classic facial cosmetics photo">Kosmetik (Klassische<br>Gesichtsbehandlung)</div>
<div class="tile cond" style="left:562px;top:934px" role="img" aria-label="Cryotherapy cold treatment photo">Kryotherapie<br>(Kältebehandlungen)</div>

<footer>
  <div class="brand-name foot-brand">Veskarin</div>
  <div class="foot-info" style="left:437px;top:1103px">
    <svg style="top:4px" width="7" height="10" viewBox="0 0 7 10"><path d="M3.5 0A3.5 3.5 0 0 0 0 3.5C0 6 3.5 10 3.5 10S7 6 7 3.5A3.5 3.5 0 0 0 3.5 0zm0 5a1.5 1.5 0 1 1 0-3 1.5 1.5 0 0 1 0 3z"/></svg>
    Your Address, Your Country<br>Your Zip Code
  </div>
  <div class="foot-info" style="left:577px;top:1102px">
    <svg style="top:4px" width="9" height="9" viewBox="0 0 11 11"><path d="M2 0l2 2.5-1 1.5c.8 1.8 2 3 3.5 3.5l1.5-1L11 8.5 9.5 11C4.5 10.5.5 6.5 0 1.5z"/></svg>
    +43 555 010 201<br>
    <svg style="top:23px" width="10" height="7" viewBox="0 0 10 7"><rect width="10" height="7"/></svg>
    info@veskarin-mail.at
  </div>
  <div class="social" style="left:705px" aria-label="Social link"></div>
  <div class="social" style="left:737px" aria-label="Social link"></div>
  <div class="social" style="left:769px" aria-label="Social link"></div>
  <div class="social" style="left:801px" aria-label="Social link"></div>
  <div class="bottom-bar">
    <span style="position:absolute;left:129px">Copyright © 2014 Veskarin. All Rights Reserved.</span>
    <span style="position:absolute;right:127px">Sitemap | Privacy Policy</span>
  </div>
</footer>
</body>
</html>
```